Residential Real Estate needs a flyer design

I need a flyer that brings all my companies together to target that person who needs to sell, rent, or refinance their home. We specialize in buying, selling, managing, and providing home loans in El Paso, TX. I have uploaded a document that will give you all my thoughts of this flyer. My companies include Brisk Mortgage Lending (Residential Mortgage Lending), Tallow Realty El Paso (Real Estate Brokerage), Quill Lease Homes El Paso (Property Management Company), MVT Capital, LLC (Real Estate Investment Manager). I believe home owners need more options in the residential real estate market. Most real estate companies can only sell a home - we can sell, rent, manage, buy or refinance a home. We have the ability to put your home on the market for sale and rent at the same time, which gives you two options at once. We also buy homes as investments (MVT Capital, LLC). All homes purchased are cash buys and can close in 10 days. We specialize in the residential real estate market in El Paso, TX (selling & buying), mortgage lending, and the property management business. Our evaluation is completely free of charge. All companies are under the same management and broker. We have a few thing we use in marketing: 1. We will sell your home in 60 days, or we will buy it....Guaranteed in writing. 2. We will sell your home in 60 days, or we will sell it for free....Guaranteed in writing. 3. We will provide you with an offer to buy your home in 24 hours guaranteed. 4. We will rent your home in 60 days, or we will manage it for free for 1 month. HOW ARE WE DIFFERENT? We are able to provide you with every possible option and educate you in each scenario with guarantees.

Target Market(s)

Expired Listings

Industry/Entity Type

Real Estate

Font styles to use
Serif

Requirements
Must have
• *Certain Restrictions Apply – Call For Details.
• This is not intended to be a solicitation if your home is currently listed with a broker.

```html
<!DOCTYPE html>
<html lang="en">
<head>
<meta charset="utf-8">
<title>Tallow Realty El Paso – Flyer</title>
<link rel="stylesheet" href="https://fonts.googleapis.com/css2?family=Noto+Serif:ital,wght@0,400;0,700;1,400;1,700&family=Carlito:wght@400;700&display=swap">
<style>
:root{
  --lime:#a6c93a;
  --lime-dark:#7fa82a;
  --navy:#1b1f4d;
  --ink:#1a1a1a;
  --red:#d42027;
  --blue-text:#1f2d8a;
  --paper:#ffffff;
  --backdrop:#d9d9d9;
}
*{box-sizing:border-box;margin:0;padding:0}
html,body{width:1200px;height:1000px;overflow:hidden;background:var(--backdrop)}
.flyer{position:absolute;left:297px;top:30px;width:717px;height:928px;background:var(--paper);overflow:hidden;
  font-family:"Carlito",Arial,sans-serif;color:var(--ink);box-shadow:0 2px 10px rgba(0,0,0,.25)}
.top-band{position:absolute;left:0;top:0;width:100%;height:16px;background:var(--lime)}
.serif{font-family:"Noto Serif",Georgia,serif}

.brand{position:absolute;left:31px;top:46px;width:160px;display:flex;align-items:flex-start;gap:6px}
.brand-mark{flex:none;width:12px;height:12px;margin-top:6px;background:var(--red)}
.brand-name{font-family:"Noto Serif",Georgia,serif;font-weight:700;font-size:20px;line-height:1.15;color:var(--ink)}

.headline{position:absolute;left:215px;top:30px;font-family:"Noto Serif",Georgia,serif;font-weight:700;font-size:25px;line-height:43px;color:var(--ink);white-space:nowrap}
.headline .alert{color:var(--red);margin-left:12px}

.house-photo{position:absolute;left:363px;top:113px;width:337px;height:160px;
  background:linear-gradient(180deg,#cfd8e2 0%,#9aa3aa 40%,#6b6f6c 70%,#7c8c4a 100%);border:2px solid #ddd}

.tab{position:absolute;left:16px;height:29px;background:var(--lime);font-family:"Noto Serif",Georgia,serif;font-weight:700;white-space:nowrap}
.tab-options{top:135px;width:265px;font-size:17px;line-height:29px;padding-left:12px;color:var(--ink)}
.tab-homes{top:363px;width:424px;font-size:18px;line-height:29px;padding-left:60px;color:var(--blue-text)}

.options{position:absolute;left:18px;top:168px;list-style:none;font-family:"Noto Serif",Georgia,serif;font-weight:700;font-size:15.5px;line-height:26px}
.options li{display:flex;align-items:center;gap:5px}
.options svg{width:20px;height:14px}

.intro{position:absolute;left:16px;top:279px;width:684px;font-size:13.2px;line-height:19px;text-align:justify}

.program-note{position:absolute;left:26px;top:397px;font-family:"Noto Serif",Georgia,serif;font-style:italic;font-size:12px;color:var(--blue-text)}

.frame{position:absolute;left:0;top:0;width:717px;height:662px}

.sales{position:absolute;left:43px;top:423px;display:grid;grid-template-columns:232px 228px auto;list-style:none;font-size:11.6px;line-height:16.3px;white-space:nowrap}

.difference{position:absolute;left:0;top:662px;width:717px;height:191px;background:var(--lime);font-family:"Noto Serif",Georgia,serif;font-weight:700}
.difference h2{position:absolute;left:17px;top:10px;font-size:17px;line-height:24px;color:var(--blue-text)}
.difference .lead{position:absolute;left:20px;top:37px;font-size:12.5px;line-height:22px;color:var(--ink)}
.guarantees{position:absolute;left:17px;top:79px;list-style:none;font-size:12.5px;line-height:22.3px;color:var(--blue-text);white-space:nowrap}
.difference .cta{position:absolute;left:17px;top:167px;font-style:italic;font-size:12.5px;line-height:18px;color:var(--ink);white-space:nowrap}

.footer{position:absolute;left:0;top:853px;width:717px;height:75px;background:var(--navy);color:#fff}
.phone{position:absolute;left:28px;top:6px;display:flex;align-items:center;gap:10px;font-family:"Noto Serif",Georgia,serif;font-weight:700;font-size:25px;line-height:36px}
.phone-icon{width:35px;height:35px;background:#fff;border-radius:6px;display:flex;align-items:center;justify-content:center}
.divider{position:absolute;left:288px;top:10px;width:2px;height:28px;background:#fff}
.address{position:absolute;left:309px;top:16px;font-family:"Noto Serif",Georgia,serif;font-weight:700;font-size:11.5px;white-space:nowrap}
.disclaimer{position:absolute;left:26px;top:45px;font-family:"Noto Serif",Georgia,serif;font-size:10px;line-height:13px}

.partners{position:absolute;left:587px;top:670px;width:113px;height:243px;background:#fff;display:flex;flex-direction:column;justify-content:space-around;align-items:center;padding:10px 6px;text-align:center}
.partner{font-family:"Noto Serif",Georgia,serif;font-size:10.5px;line-height:1.25;color:#2b3a2b}
.partner-dot{display:block;width:18px;height:18px;border-radius:50%;background:var(--lime-dark);margin:0 auto 5px}
</style>
</head>
<body>
<main class="flyer">
  <div class="top-band"></div>

  <div class="brand"><span class="brand-mark"></span><span class="brand-name">Tallow Realty El Paso</span></div>

  <h1 class="headline">Give yourself more options.<br>Don’t let your <span class="alert">HOME EXPIRE AGAIN.</span></h1>

  <div class="house-photo" role="img" aria-label="Photo of a two-storey grey family home with a white porch under a cloudy sky"></div>

  <div class="tab tab-options">GIVE YOURSELF OPTIONS</div>

  <ul class="options">
    <li><svg viewBox="0 0 20 14"><polygon points="2,12 10,2 18,12" fill="none" stroke="#7fa82a" stroke-width="1.6"/></svg>We can sell your Home.</li>
    <li><svg viewBox="0 0 20 14"><polygon points="2,12 10,2 18,12" fill="none" stroke="#7fa82a" stroke-width="1.6"/></svg>Rent your Home.</li>
    <li><svg viewBox="0 0 20 14"><polygon points="2,12 10,2 18,12" fill="none" stroke="#7fa82a" stroke-width="1.6"/></svg>Refinance your home.</li>
    <li><svg viewBox="0 0 20 14"><polygon points="2,12 10,2 18,12" fill="none" stroke="#7fa82a" stroke-width="1.6"/></svg>Buy your home.</li>
  </ul>

  <p class="intro">We have the ability to put your home on the market for sale and rent at the same time, which gives you two options at once. All homes purchased are cash buys and can close in 10 days. We specialize in the residential real estate market (selling &amp; buying), mortgage lending, and the property management business.  Our evaluation is completely free of charge.  All the companies below are under the same management and broker.</p>

  <div class="tab tab-homes">Homes Purchased this year (2014)</div>

  <svg class="frame" viewBox="0 0 717 662" aria-hidden="true">
    <polygon points="276,166 343,166 305,123" fill="var(--paper)" stroke="var(--lime-dark)" stroke-width="1.5"/>
    <polygon points="29,389 67,389 48,368" fill="var(--paper)" stroke="var(--paper)" stroke-width="1"/>
    <polyline points="503,420 603,353 700,420" fill="none" stroke="var(--lime-dark)" stroke-width="3"/>
    <rect x="18" y="420" width="682" height="236" fill="none" stroke="var(--lime-dark)" stroke-width="3"/>
  </svg>

  <p class="program-note">All homes purchased in this program by our investors are used for rental purposes.</p>

  <ol class="sales">
    <li>1. 10815 Pleasant Hill ($91,000)</li><li>2. 12742 Tierra Sonora ($120,000)</li><li>3. 3164 Coyote Park ($162,500)</li>
    <li>4. 12903 Destiny ($120,000)</li><li>5. 572 Via De Los Arobles ($218,000)</li><li>6. 3291 Bell Point ($98,404)</li>
    <li>7. 7213 Copper Nail ($100,000)</li><li>8. 11548 Charles Boyle ($178,000)</li><li>9. 5517 Ignacio Frias ($147,500)</li>
    <li>10. 11832 Auburn Sand ($86,500)</li><li>11. 10971 Cattle Ranch ($118,000)</li><li>12. 3172 Tierra Encino ($92,000)</li>
    <li>13. 3148 Tierra Cuervo ($167,500)</li><li>14. 11637 Clear Lake ($83,000)</li><li>15. 14129 Tierra Halcon ($86,000)</li>
    <li>16. 738 Desert Spring ($86,800)</li><li>17. 11925 Jim Webb ($86,000)</li><li>18. 11283 Northview ($152,000)</li>
    <li>19. 12097 Jose Cisneros ($95,000)</li><li>20. 12868 Tierra Ayala ($105,320)</li><li>21. 547 Paseo De Fe ($119,000)</li>
    <li>22. 11559 Lucio Moreno ($150,000)</li><li>23. 10583 Silvercloud ($85,000)</li><li>24. 3225 Emerald Point ($107,660)</li>
    <li>25. 719 Desert Sage ($84,000)</li><li>26. 12534 Flora Alba ($84,362)</li><li>27. 14216 Desert Fire ($80,426)</li>
    <li>28. 11147 Redstone Cove ($121,500)</li><li>29. 368 Jim Hofher ($80,000)</li><li>30. 6204 Bandolero ($157,000)</li>
    <li>31. 12326 Tierra Apache ($81,000)</li><li>32. 482 Cactus Crossing ($85,000)</li><li>33. 5593 Ignacio Frias ($149,000)</li>
    <li>34. 14249 Haciendas Rock ($101,550)</li><li>35. 6287 Oryx Circle ($68,298)</li><li>36. 7958 Night Fall ($108,000)</li>
    <li>37. 12672 Sun Empress ($157,000)</li><li>38. 11473 Pifas Nevarez ($138,500)</li><li>39. 1381 Fito Hernandez ($143,500)</li>
    <li>40. 10786 Pleasant Sand ($125,000)</li>
  </ol>

  <section class="difference">
    <h2>HOW ARE WE DIFFERENT?</h2>
    <p class="lead">We are able to provide you with every possible option<br>and educate you in each scenario.</p>
    <ol class="guarantees">
      <li>1. We will sell your home in 60 days, or we will buy it....Guaranteed in writing.</li>
      <li>2. We will sell your home in 60 days, or we will sell it for free....Guaranteed in writing.</li>
      <li>3. We will provide you with an offer to buy your home in 24 hours guaranteed.</li>
      <li>4. We will rent your home in 60</li>
    </ol>
    <p class="cta">CALL US TODAY TO SCHEDULE AN APPOINTMENT  COMPLETELY FREE OF CHARGE.</p>
  </section>

  <footer class="footer">
    <div class="phone">
      <span class="phone-icon"><svg width="20" height="22" viewBox="0 0 20 22"><path d="M5 1 L8 6 L6 8 Q8 13 12 16 L14 14 L19 17 L17 21 Q9 21 4 13 Q1 7 2 2 Z" fill="var(--navy)"/></svg></span>
      915-555-0142
    </div>
    <span class="divider"></span>
    <span class="address">418 N. Copper Ridge, B-2 El Paso, TX 79912</span>
    <p class="disclaimer">Note: This is not intended to be a solicitation if your home is currently listed with a broker.<br>*Certain Restrictions Apply – Call For Details.</p>
  </footer>

  <aside class="partners">
    <div class="partner"><span class="partner-dot"></span>MVT Capital, LLC</div>
    <div class="partner"><span class="partner-dot"></span>Brisk Mortgage Lending</div>
    <div class="partner"><span class="partner-dot"></span>Quill Lease Homes El Paso</div>
  </aside>
</main>
</body>
</html>
```